Lydia Vandermere personal business/name cards and stationery brief

I am looking for a simple design on my personal business cards, that I may use for all my stationery. All my stationery would be cream or ivory textured card, or cream/ivory quality paper. I am director of my family company and also property developer. But am wishing to have basic business cards that I can use across both businesses. I do not wish to have a title, just my initials as a focal point.
Target Market(s)
These are my personal business cards and stationery. I am looking for an elegant, relatively understated design that exudes wealth. There is no target audience, other than clients or people I already do business with. However design must be stylish and timeless.
If I am handing out my business card to anyone I do not do business with, or they are not contracting to me or my company currently, then i would like the target audience to wish they were.
I am 54 yeas of age, and my business cards must denote respect and class.
Industry/Entity Type
Business
Contact Information for Business Card
LV
Lydia Vandermere
Justice of the Peace
Possible rear of card
Mobile number
Email
Font styles to use
Requirements
Must have
- LV to be somehow entwined as a logo on the front of the card above my name
- These cards must state that I am a Justice of the Peace
- Colours only ivory or cream card with texture, and gold elegant font.
- Must be able to be used on all my stationery products
- Must be elegant, timeless and not cluttered
- Below are just some design I like. There is something in each design I like.
Nice to have
- I would like my initials to be the centre piece of the card. Somehow entwined together elegantly in a logo of sorts that I can use across all my stationery. But if not my initials, then something that is different and stands out from the rest.
Should not have
- Not gawdy or young. No colour. Nothing outlandish.

```html
<!DOCTYPE html>
<html lang="en">
<head>
<meta charset="utf-8">
<title>Lydia Vandermere — Business Card</title>
<link rel="stylesheet" href="https://fonts.googleapis.com/css2?family=Raleway:wght@200;300&display=swap">
<style>
  :root {
    --backdrop: #e9e6e1;
    --card-ivory: #efe6d6;
    --card-ivory-light: #f5eee2;
    --card-taupe: #7b7068;
    --card-taupe-light: #85796f;
    --gold: #c98a4a;
    --gold-soft: #c4925f;
    --card-shadow: rgba(60, 50, 40, 0.28);
  }
  * { margin: 0; padding: 0; box-sizing: border-box; }
  html, body {
    width: 1200px;
    height: 900px;
    overflow: hidden;
    background: var(--backdrop);
    font-family: "Raleway", sans-serif;
  }
  .sheet {
    width: 1200px;
    height: 900px;
    display: flex;
    flex-direction: column;
    align-items: center;
    justify-content: center;
    gap: 56px;
  }
  .card {
    width: 640px;
    height: 366px;
    box-shadow: 0 6px 18px var(--card-shadow);
    display: flex;
    align-items: center;
    justify-content: center;
  }
  .card--back {
    background: radial-gradient(ellipse at 40% 40%, var(--card-taupe-light), var(--card-taupe));
  }
  .card--front {
    background: radial-gradient(ellipse at 50% 35%, var(--card-ivory-light), var(--card-ivory));
  }
  .contact {
    text-align: center;
    color: var(--gold-soft);
    font-weight: 300;
  }
  .contact__name {
    font-size: 30px;
    font-weight: 200;
    letter-spacing: 1px;
  }
  .contact__title {
    font-size: 15px;
    margin-top: 4px;
    letter-spacing: 0.5px;
  }
  .contact__rule {
    width: 14px;
    height: 1px;
    background: var(--gold-soft);
    margin: 12px auto 10px;
  }
  .contact__line {
    font-size: 15px;
    line-height: 1.45;
    letter-spacing: 0.5px;
  }
  .monogram {
    color: var(--gold);
    font-size: 200px;
    font-weight: 300;
    line-height: 1;
    letter-spacing: -4px;
  }
</style>
</head>
<body>
  <main class="sheet">
    <section class="card card--back">
      <div class="contact">
        <p class="contact__name">Lydia Vandermere</p>
        <p class="contact__title">Justice of the Peace</p>
        <div class="contact__rule"></div>
        <p class="contact__line">+61 402 318 564</p>
        <p class="contact__line">hello@vandermere.co</p>
      </div>
    </section>
    <section class="card card--front">
      <p class="monogram">LV</p>
    </section>
  </main>
</body>
</html>
```